Business Card Design - Marla_BPH

We need a Business card for a new company based in Sydney Australia.
We distribute children's toys and educational products to Australian retailers.
Our clients are overseas manufacturers, Australian retail shop owners, schools, educational centres.
The design should communicate education and development for children.
The colours should be Australian primary bold colours. Green and Gold is an option to symbolise Australia.

Target Market(s)

Overseas manufacturers, Australian retail shop owners, Trade fairs

Industry/Entity Type

Education

Requirements
Must have
• BUSINESS CARD TO READ:

Marla Trescott
Managing Director

Tel: +61 452 918 306
Fax: +61 2 9364 2187
Marla@BrightPuddleHub.com.au

Bright Puddle Hub Pty Ltd
4/238 Wattlefield Rd.
Kestrel Cove, Sydney, NSW
Australia, 2026
www.BrightPuddleHub.com.au
Nice to have
• BACK OF THE BUSINESS CARD:

Images:

Fenna Ostrava
Rupert Tiny Snow Hare
Tiny Greta & Olof

same as business card example uploaded

```html
<!DOCTYPE html>
<html lang="en">
<head>
<meta charset="utf-8">
<title>Bright Puddle Hub – Business Card</title>
<link rel="stylesheet" href="https://fonts.googleapis.com/css2?family=Sniglet:wght@400;800&family=Nunito+Sans:wght@700&display=swap">
<style>
  :root {
    --card-bg: #ffffff;
    --ink: #1c1c1c;
    --brand-blue: #1d3fd0;
    --brand-dot: #8f8fd6;
    --band-gold: #d9bf38;
    --plush-light: #f3efea;
    --plush-mid: #e6ddd3;
  }
  html, body {
    margin: 0;
    padding: 0;
    width: 1200px;
    height: 651px;
    overflow: hidden;
    background: var(--card-bg);
  }
  .card {
    position: relative;
    width: 1200px;
    height: 651px;
    background: var(--card-bg);
    overflow: hidden;
    font-family: "Sniglet", "Comic Sans MS", cursive;
    font-weight: 800;
    color: var(--ink);
  }
  .product-photo {
    position: absolute;
    left: 18px;
    top: 112px;
    width: 480px;
    height: 456px;
    border-radius: 46% 42% 30% 30%;
    background: radial-gradient(ellipse at 45% 40%, var(--plush-light) 0%, var(--plush-mid) 75%, #ffffff 100%);
  }
  .brand {
    position: absolute;
    right: 28px;
    top: 40px;
    display: flex;
    align-items: center;
    gap: 12px;
  }
  .brand-dot {
    width: 46px;
    height: 46px;
    border-radius: 50%;
    background: var(--brand-dot);
  }
  .brand-name {
    font-size: 50px;
    line-height: 1;
    color: var(--brand-blue);
    white-space: nowrap;
  }
  .brand-tagline {
    position: absolute;
    right: 40px;
    top: 138px;
    font-family: "Nunito Sans", Arial, sans-serif;
    font-weight: 700;
    font-size: 19px;
    color: var(--ink);
  }
  .contact {
    position: absolute;
    left: 541px;
    top: 216px;
  }
  .contact-name {
    margin: 0;
    font-size: 32px;
    line-height: 42px;
    font-weight: 800;
  }
  .contact-role {
    margin: 0 0 56px;
    font-size: 26px;
    line-height: 40px;
  }
  .contact-lines {
    list-style: none;
    margin: 0;
    padding: 0;
    font-size: 26px;
    line-height: 45px;
  }
  .company-address {
    position: absolute;
    right: 40px;
    top: 222px;
    margin: 0;
    font-style: normal;
    font-weight: 400;
    font-size: 19px;
    line-height: 28px;
    text-align: right;
  }
  .web-band {
    position: absolute;
    left: 493px;
    bottom: 0;
    width: 707px;
    height: 46px;
    background: var(--band-gold);
  }
  .web-address {
    position: absolute;
    left: 48px;
    top: 4px;
    font-size: 26px;
    line-height: 38px;
  }
</style>
</head>
<body>
  <main class="card">
    <div class="product-photo" role="img" aria-label="Photo of a cream plush baby polar bear toy sitting"></div>

    <div class="brand">
      <span class="brand-dot"></span>
      <span class="brand-name">Bright Puddle Hub</span>
    </div>
    <div class="brand-tagline">Australian Distributor</div>

    <section class="contact">
      <h1 class="contact-name">Marla Trescott</h1>
      <p class="contact-role">Managing Director</p>
      <ul class="contact-lines">
        <li>Tel: +61 452 918 306</li>
        <li>Fax: +61 2 9364 2187</li>
        <li>Marla@BrightPuddleHub.com.au</li>
      </ul>
    </section>

    <address class="company-address">
      Bright Puddle Hub Pty Ltd<br>
      4/238 Wattlefield Rd.<br>
      Kestrel Cove, Sydney, NSW<br>
      Australia, 2026
    </address>

    <footer class="web-band">
      <span class="web-address">www.BrightPuddleHub.com.au</span>
    </footer>
  </main>
</body>
</html>
```